A brochure website design
Product: Nuvel coconut yogurt
Specialty of the product:
Nuvel coconut yogurt is a non dairy yogurt using coconut cream powder and coconut water as its major ingredients. It contains live cultures and is a great alternatives to dairy yogurt.
It is gluten free, soy free, preservative free, lactose free, non-GMO and no artificial sweetener. It is a great choice for paleo diet.
4. About Nuvel
Nuvel is developed by a group of coconut lovers who believe that promoting vegan based diet can contribute to the wellness of the world and the sustainability of living. Our vision is to end cruelty to animal and minimise the world’s reliance on milk farming. We believe that cow milk is belonged to cow BB and God has already provided coconut to us which is actually more suitable to human’s body than dairy product.
5. Our products
Nuvel coconut yogurt 120g
Nuvel coconut yogurt with raspberry 150g
6. Nuvel recipes
7. About coconut
8. Contact us
9. Stores finder
Target Market(s)
Age 18 to 50 . People looking for life style and healthy diet.
Industry/Entity Type
Product
Number of Pages Required
5+ page
Look and feel
Each slider illustrates characteristics of the customer's brand and the style your logo design should communicate.

```html
<!DOCTYPE html>
<html lang="en">
<head>
<meta charset="utf-8">
<title>Nuvel Coconut Yoghurt</title>
<link href="https://fonts.googleapis.com/css2?family=Lato:wght@400;700&family=Open+Sans:wght@400;600;700&display=swap" rel="stylesheet">
<style>
:root{
  --green:#3b9a41;
  --green-dark:#237a2c;
  --green-band:#2f8a35;
  --teal:#2fa3b5;
  --text:#444;
  --muted:#666;
  --light-bg:#f2f2f2;
  --card-bg:#e6e6e6;
  --footer-bg:#2b2b2b;
  --footer-text:#ddd;
  --white:#fff;
}
*{box-sizing:border-box;margin:0;padding:0}
html,body{width:1200px;height:3051px;overflow:hidden}
body{position:relative;background:var(--white);font-family:"Open Sans",Arial,sans-serif;color:var(--text)}
.abs{position:absolute}
.section-title{font-family:"Lato",Arial,sans-serif;font-weight:700;color:var(--green);font-size:29px;text-align:center}
.title-rule{width:120px;height:2px;background:var(--green);margin:18px auto 0}

/* header */
.site-header{left:0;top:0;width:1200px;height:102px;background:var(--white);border-top:4px solid var(--green)}
.brand{left:100px;top:24px;display:flex;align-items:center;gap:14px}
.brand-mark{width:56px;height:56px;border-radius:50%;background:var(--green)}
.brand-name{font-family:"Lato",Arial,sans-serif;font-weight:700;font-size:20px;line-height:24px;color:var(--teal);text-transform:uppercase}
.main-nav{right:98px;top:40px;display:flex;gap:26px;font-family:"Open Sans",sans-serif;font-size:14px;color:#333}
.main-nav a{color:#333;text-decoration:none;padding-bottom:12px}
.main-nav a.active{color:var(--green);border-bottom:2px solid var(--green)}

/* hero */
.hero{left:0;top:102px;width:1200px;height:508px;overflow:hidden}
.hero-photo{position:absolute;inset:0;background:linear-gradient(180deg,#c8d6d8 0%,#b8c4b4 25%,#c4aa7a 55%,#b08f5e 100%)}
.hero-title{left:100px;top:88px;color:var(--white);font-family:"Lato",sans-serif;font-weight:700;font-size:42px;line-height:58px;text-transform:uppercase}
.hero-dots{left:100px;top:240px;display:flex;gap:4px}
.hero-dots span{width:14px;height:14px;border-radius:50%;border:2px solid var(--white)}
.hero-dots span.on{background:var(--teal)}
.hero-band{left:0;bottom:0;width:1200px;height:130px}
.hero-caption{left:0;top:450px;width:1200px;text-align:center;color:var(--white);font-weight:600;font-size:19px;letter-spacing:.3px}

/* welcome */
.welcome{left:0;top:610px;width:1200px;height:400px;background:var(--light-bg)}
.welcome-curve{left:0;top:960px;width:1200px;height:60px}
.welcome .section-title{margin-top:52px}
.welcome-text{width:910px;margin:38px auto 0;text-align:center;font-size:14px;line-height:26px;color:var(--muted)}
.btn-outline{display:block;width:130px;height:46px;margin:36px auto 0;border:2px solid var(--green-dark);color:var(--green-dark);font-size:13px;font-weight:600;text-align:center;line-height:42px;text-transform:uppercase}

/* recipes */
.recipes-title{left:0;top:1050px;width:1200px}
.recipe{top:1139px;width:320px}
.recipe-photo{width:320px;height:234px;border:2px solid var(--green)}
.recipe-name{margin-top:20px;font-family:"Lato",sans-serif;font-weight:700;font-size:20px;color:var(--green)}
.recipe-text{margin-top:16px;font-size:13px;line-height:24px;color:var(--muted);text-align:justify}
.btn-solid{display:inline-block;margin-top:16px;width:104px;height:38px;line-height:38px;text-align:center;background:var(--green);color:var(--white);font-size:13px;font-weight:600;text-transform:uppercase}
.recipe-rule{margin-top:16px;height:3px;background:var(--green)}

/* products */
.products{left:0;top:1600px;width:1200px;height:690px}
.products-title{left:0;top:1733px;width:1200px}
.products-title .section-title{color:var(--white)}
.products-title .title-rule{background:var(--white)}
.product-card{top:1841px;width:308px;height:315px;background:var(--card-bg);border-radius:8px;text-align:center}
.product-photo{width:130px;height:130px;margin:32px auto 0;border-radius:10px;background:linear-gradient(180deg,#d8eff0,#3fb7b6 50%,#e9e9e9)}
.product-name{margin-top:58px;font-size:19px;color:#222}
.product-qty{margin-top:8px;font-size:18px;font-weight:700;color:var(--green)}

/* wellness */
.wellness{left:98px;top:2296px;width:580px}
.wellness h2{font-family:"Lato",sans-serif;font-weight:700;font-size:27px;color:var(--green)}
.wellness-lead{margin-top:20px;font-size:16px;line-height:28px;color:#222}
.wellness-list{margin-top:22px;list-style:none}
.wellness-list li{position:relative;padding-left:24px;font-size:13px;line-height:28px;color:#333;margin-bottom:2px}
.wellness-list li::before{content:"";position:absolute;left:0;top:9px;width:8px;height:8px;border:2px solid var(--green);border-radius:50%}
.coconut-photo{left:702px;top:2300px;width:406px;height:290px;border-radius:12px;background:linear-gradient(160deg,#c9a27a 0%,#8a5a34 45%,#efe6d6 70%,#6f9a48 100%)}

/* footer */
.footer{left:0;top:2600px;width:1200px;height:451px}
.footer-brand{left:98px;top:2796px;display:flex;align-items:center;gap:14px}
.footer-brand .brand-mark{width:58px;height:58px}
.footer-brand .brand-name{color:var(--white);font-size:18px}
.footer-col h3{font-family:"Open Sans",sans-serif;font-size:16px;font-weight:700;color:var(--white);text-transform:uppercase}
.footer-col h3::after{content:"";display:block;width:44px;height:2px;background:var(--white);margin-top:10px}
.quick-links{left:403px;top:2696px}
.quick-links ul{list-style:none;margin-top:26px}
.quick-links li{font-size:14px;color:var(--footer-text);line-height:31px}
.contact-info{left:559px;top:2696px;width:250px}
.contact-row{display:flex;align-items:flex-start;gap:18px;margin-top:24px}
.contact-icon{flex:none;width:38px;height:38px;border:2px solid var(--white);border-radius:50%;display:flex;align-items:center;justify-content:center}
.contact-icon svg{display:block}
.contact-label{display:block;color:var(--white);font-size:14px;font-weight:700;text-transform:uppercase}
.contact-detail{display:block;color:var(--footer-text);font-size:12.5px;line-height:22px}
.contact-form{left:830px;top:2696px;width:272px}
.form-row{display:flex;gap:16px;margin-top:28px}
.field{height:36px;border:1px solid #bbb;border-radius:3px;color:var(--white);font-size:11px;padding:9px 10px}
.field.half{width:128px}
.field.area{width:272px;height:66px;margin-top:8px}
.btn-send{display:inline-block;margin-top:14px;width:118px;height:36px;line-height:36px;text-align:center;background:var(--white);color:#333;border-radius:3px;font-size:11px;text-transform:uppercase}
.footer-rule{left:98px;top:2984px;width:1004px;height:1px;background:#888}
.copyright{left:98px;top:3007px;font-size:13px;color:var(--footer-text)}
.social{left:948px;top:2998px;display:flex;gap:10px}
.social span{width:34px;height:34px;border:2px solid var(--white);border-radius:50%}
</style>
</head>
<body>

<header class="site-header abs">
  <div class="brand abs"><span class="brand-mark"></span><span class="brand-name">Nuvel<br>Coconut Yoghurt</span></div>
  <nav class="main-nav abs">
    <a class="active">Home</a><a>About</a><a>Products</a><a>Nuvel Recipes</a><a>About Coconut</a><a>Contact Us</a><a>Store finder</a>
  </nav>
</header>

<section class="hero abs">
  <div class="hero-photo" role="img" aria-label="Two fresh coconuts with drinking straws on a sandy beach beside a striped towel"></div>
  <h1 class="hero-title abs">Nuvel Coconut Yogurt<br>Non Dairy Yogurt</h1>
  <div class="hero-dots abs"><span class="on"></span><span></span><span></span><span></span><span></span></div>
  <svg class="hero-band abs" viewBox="0 0 1200 130" preserveAspectRatio="none">
    <path d="M0 30 C300 0 500 60 800 30 C1000 10 1100 40 1200 20 L1200 130 L0 130 Z" fill="var(--green-band)"/>
  </svg>
  <p class="hero-caption abs">IT CONTAINS LIVE CULTURES AND IS A GREAT ALTERNATIVES TO DAIRY YOGURT.</p>
</section>

<section class="welcome abs">
  <h2 class="section-title">Welcome To Nuvel Coconut Yogurt</h2>
  <div class="title-rule"></div>
  <p class="welcome-text">Nuvel coconut yogurt is a non dairy yogurt using coconut cream powder and coconut water as its major ingredients. It contains live cultures and is a great alternatives to dairy yogurt. It is gluten free, soy free, preservative free, lactose free, non-GMO and no artificial sweetener. It is a great choice for paleo diet. Nuvel is developed by a group of coconut lovers who believe that promoting vegan based diet can contribute to the wellness of the world and the sustainability of living.</p>
  <a class="btn-outline">Read More</a>
</section>
<svg class="welcome-curve abs" viewBox="0 0 1200 60" preserveAspectRatio="none">
  <path d="M0 0 L1200 0 L1200 10 Q600 80 0 10 Z" fill="var(--light-bg)"/>
</svg>

<div class="recipes-title abs">
  <h2 class="section-title">Our Nuvel Recipes</h2>
  <div class="title-rule"></div>
</div>

<article class="recipe abs" style="left:98px">
  <div class="recipe-photo" role="img" aria-label="Glasses of coconut ice cream dessert on a wooden board" style="background:linear-gradient(135deg,#3a2418,#8a6a52 50%,#e8e0d6)"></div>
  <h3 class="recipe-name">Coconut Lovers</h3>
  <p class="recipe-text">Nuvel is developed by a group of coconut lovers who believe that promoting vegan based diet can contribute to the wellness of the world and the sustainability of living.</p>
  <a class="btn-solid">Read More</a>
  <div class="recipe-rule"></div>
</article>
<article class="recipe abs" style="left:439px">
  <div class="recipe-photo" role="img" aria-label="Bowl of coconut yogurt topped with coconut pieces on a checked cloth" style="background:linear-gradient(135deg,#9a8d6c,#d8d8d8 45%,#f4f4f2 60%,#8f9aa4)"></div>
  <h3 class="recipe-name">Sustainability Of Living</h3>
  <p class="recipe-text">Nuvel is developed by a group of coconut lovers who believe that promoting vegan based diet can contribute to the wellness of the world and the sustainability of living.</p>
  <a class="btn-solid">Read More</a>
  <div class="recipe-rule"></div>
</article>
<article class="recipe abs" style="left:781px">
  <div class="recipe-photo" role="img" aria-label="Yogurt bowl with fruit and granola beside a jug of milk and nuts" style="background:linear-gradient(135deg,#e8e2da,#b85a6a 40%,#8a5a34 70%,#5a3a22)"></div>
  <h3 class="recipe-name">Artificial Sweetener</h3>
  <p class="recipe-text">Nuvel is developed by a group of coconut lovers who believe that promoting vegan based diet can contribute to the wellness of the world and the sustainability of living.</p>
  <a class="btn-solid">Read More</a>
  <div class="recipe-rule"></div>
</article>

<svg class="products abs" viewBox="0 0 1200 690" preserveAspectRatio="none">
  <defs><linearGradient id="leafGreen" x1="0" y1="0" x2="1" y2="1"><stop offset="0" stop-color="#2a8a30"/><stop offset="1" stop-color="#1f7326"/></linearGradient></defs>
  <path d="M0 60 Q600 -30 1200 60 L1200 640 Q600 700 0 640 Z" fill="url(#leafGreen)"/>
</svg>
<div class="products-title abs">
  <h2 class="section-title">OUR YOGURT PRODUCTS</h2>
  <div class="title-rule"></div>
</div>
<div class="product-card abs" style="left:98px">
  <div class="product-photo" role="img" aria-label="Cup of Nuvel coconut yogurt"></div>
  <p class="product-name">Nuvel Coconut Yogurt</p>
  <p class="product-qty">Quantity:120g</p>
</div>
<div class="product-card abs" style="left:447px">
  <div class="product-photo" role="img" aria-label="Cup of Nuvel coconut yogurt with raspberry"></div>
  <p class="product-name">Nuvel Coconut Yogurt Raspberry</p>
  <p class="product-qty">Quantity:150g</p>
</div>
<div class="product-card abs" style="left:795px">
  <div class="product-photo" role="img" aria-label="Cup of Nuvel coconut yogurt"></div>
  <p class="product-name">Nuvel Coconut Yogurt</p>
  <p class="product-qty">Quantity:170g</p>
</div>

<section class="wellness abs">
  <h2>Wellness Of The World</h2>
  <p class="wellness-lead">Nuvel is developed by a group of coconut lovers who believe that promoting vegan based diet can contribute to the wellness.</p>
  <ul class="wellness-list">
    <li>Our vision is to end cruelty to animal and minimise the world's reliance on milk farming.</li>
    <li>We believe that cow milk is belonged to cow BB and God has already provided coconut.</li>
    <li>It is gluten free, soy free, preservative free, lactose free, non-GMO and no artificial sweetener.</li>
  </ul>
</section>
<div class="coconut-photo abs" role="img" aria-label="Photo of a whole coconut and a split coconut half resting on palm leaves"></div>

<svg class="footer abs" viewBox="0 0 1200 451" preserveAspectRatio="none">
  <path d="M0 14 Q600 70 1200 14 L1200 451 L0 451 Z" fill="var(--footer-bg)"/>
</svg>
<div class="footer-brand abs"><span class="brand-mark"></span><span class="brand-name">Nuvel<br>Coconut Yoghurt</span></div>

<div class="footer-col quick-links abs">
  <h3>Quick Links</h3>
  <ul><li>› Home</li><li>› About Us</li><li>› Products</li><li>› Nuvel Recipes</li><li>› Store finder</li><li>› Contact us</li></ul>
</div>

<div class="footer-col contact-info abs">
  <h3>Contact Us</h3>
  <div class="contact-row">
    <div class="contact-icon"><svg width="14" height="18" viewBox="0 0 14 18"><path d="M7 0C3 0 0 3 0 7c0 5 7 11 7 11s7-6 7-11c0-4-3-7-7-7z" fill="#fff"/><circle cx="7" cy="7" r="2.5" fill="#2b2b2b"/></svg></div>
    <div><strong class="contact-label">Nuvel Coconut Yogurt,</strong><span class="contact-detail">Fernvale Lane, Harbourside, Westport 12, Ireland.</span></div>
  </div>
  <div class="contact-row">
    <div class="contact-icon"><svg width="12" height="18" viewBox="0 0 12 18"><rect x="1" y="1" width="10" height="16" rx="2" fill="none" stroke="#fff" stroke-width="2"/><circle cx="6" cy="14" r="1" fill="#fff"/></svg></div>
    <div><strong class="contact-label">Phone:</strong><span class="contact-detail">180 044 7190</span></div>
  </div>
  <div class="contact-row">
    <div class="contact-icon"><svg width="16" height="12" viewBox="0 0 16 12"><rect width="16" height="12" rx="1" fill="#fff"/><path d="M0 1l8 6 8-6" fill="none" stroke="#2b2b2b" stroke-width="1.5"/></svg></div>
    <div><strong class="contact-label">Mail:</strong><span class="contact-detail">info@nuvelcoconutyogurt.example</span></div>
  </div>
</div>

<div class="footer-col contact-form abs">
  <h3>Contact Form</h3>
  <div class="form-row"><span class="field half">Name</span><span class="field half">Phone</span></div>
  <div class="field area">Message</div>
  <span class="btn-send">Send Message</span>
</div>

<div class="footer-rule abs"></div>
<p class="copyright abs">Copyright © 2016 Nuvel coconut yogurt. All Right Reserved</p>
<div class="social abs"><span></span><span></span><span></span><span></span></div>

</body>
</html>
```